Lantern of Renewal needs a business card design

I need a business card design for my company to promote my new Christian non-fiction book, "Where The River Bends Home." I also want it to promote my web site, www.lanternofrenewalbks.com. The book is about empowering people to be transformed through a deeper relationship with God. I am picturing a design with a dove over water that matches the colors of my book cover, blue, white, yellow, and orange. Fire and light would also be possible elements of the design. I would like to be able to use the dove by itself as a logo for my business. This is my first book and I do not know if others will follow. The name of my publishing company is Silver Harvest Press, named after Gideon in the Bible story from the book of Judges. My book was independently published and was recently selected as a finalist for the 2015 Bright Horizon SMALLPRESS book award in the Christian non-fiction genre.

Target Market(s)

People who are hungry for more of God and who want to experience deep change in their lives.

Industry/Entity Type

Business

Contact Information for Business Card

Dana Whitcombe
Author
Where The River Bends Home
4287 Maple Orchard Lane
Austin, Texas 78651-2097
512-555-0143 512-555-0178
dana-whitcombe@examplemail.net
www.lanternofrenewalbks.com

Colors
0355a3
3377b5
85acd3
cedeed
fbee3e
ffc214

Requirements
Must have
• A dove with a blue background, peaceful and appealing
Nice to have
• Water and fire or light
Should not have
• Violence or fear-producing images

```html
<!DOCTYPE html>
<html lang="en">
<head>
<meta charset="utf-8">
<title>Dana Whitcombe – Business Card</title>
<link rel="stylesheet" href="https://fonts.googleapis.com/css2?family=Montserrat:wght@400;500&family=Tinos&display=swap">
<style>
  :root {
    --stage: #b2b5b6;
    --navy: #0b1f4e;
    --navy-deep: #0a1a45;
    --sea: #3d62a0;
    --sea-light: #5a80bd;
    --spray: #c8d6ee;
    --white: #ffffff;
    --title-ink: #0d2152;
  }
  * { margin: 0; padding: 0; box-sizing: border-box; }
  html, body {
    width: 1200px;
    height: 1000px;
    overflow: hidden;
    background: #ffffff;
  }
  .stage {
    position: absolute;
    left: 61px;
    top: 71px;
    width: 1078px;
    height: 867px;
    background: var(--stage);
  }
  .card {
    position: absolute;
    left: 252px;
    top: 267px;
    width: 715px;
    height: 407px;
    overflow: hidden;
    background: var(--navy);
    font-family: "Montserrat", Arial, sans-serif;
    color: var(--white);
  }
  .card-art {
    position: absolute;
    inset: 0;
    width: 715px;
    height: 407px;
  }
  .contact {
    position: absolute;
    left: 358px;
    top: 35px;
    font-size: 15px;
    font-weight: 500;
    letter-spacing: 0.2px;
  }
  .contact .address { line-height: 19px; }
  .contact .address .zip { display: block; margin-top: 3px; }
  .contact .phones {
    display: flex;
    align-items: center;
    margin-top: 13px;
    font-size: 16px;
  }
  .contact .phones .label { margin-right: 10px; }
  .contact .phones .divider {
    display: inline-block;
    width: 2px;
    height: 24px;
    background: var(--white);
    margin: 0 12px;
  }
  .contact .email { margin-top: 17px; }
  .contact .web { margin-top: 19px; }
  .book-title {
    position: absolute;
    left: 54px;
    top: 279px;
    font-family: "Tinos", "Times New Roman", serif;
    font-size: 35px;
    line-height: 41px;
    color: var(--title-ink);
    white-space: nowrap;
  }
  .author {
    position: absolute;
    left: 350px;
    top: 293px;
    width: 220px;
    text-align: center;
    font-weight: 400;
  }
  .author .name { font-size: 27px; line-height: 32px; }
  .author .role { font-size: 22px; line-height: 30px; margin-top: 2px; }
</style>
</head>
<body>
  <div class="stage"></div>

  <section class="card" aria-label="Business card for Dana Whitcombe, author">
    <svg class="card-art" viewBox="0 0 715 407" xmlns="http://www.w3.org/2000/svg">
      <defs>
        <linearGradient id="sea-fill" x1="0" y1="0" x2="1" y2="1">
          <stop offset="0" stop-color="#3a5d9b"/>
          <stop offset="0.6" stop-color="#4469a6"/>
          <stop offset="1" stop-color="#395c98"/>
        </linearGradient>
        <radialGradient id="spray-fill" cx="0.5" cy="0.5" r="0.5">
          <stop offset="0" stop-color="#c8d6ee" stop-opacity="0.85"/>
          <stop offset="1" stop-color="#c8d6ee" stop-opacity="0"/>
        </radialGradient>
        <radialGradient id="dove-glow" cx="0.5" cy="0.5" r="0.5">
          <stop offset="0" stop-color="#ffffff" stop-opacity="0.95"/>
          <stop offset="0.45" stop-color="#e6ecf8" stop-opacity="0.6"/>
          <stop offset="1" stop-color="#ffffff" stop-opacity="0"/>
        </radialGradient>
      </defs>

      <g class="sea-photo" role="img" aria-label="Photo of ocean waves crashing into white spray against dark rocks">
        <path d="M0,125 C150,190 300,228 420,255 C560,285 640,340 700,407 L0,407 Z" fill="url(#sea-fill)"/>
        <ellipse cx="170" cy="330" rx="130" ry="90" fill="url(#spray-fill)"/>
      </g>

      <path class="swoosh" d="M0,60 C150,140 300,185 420,212 C560,242 650,295 715,375 L715,392 C650,312 560,258 420,230 C300,205 150,165 0,110 Z" fill="var(--white)"/>

      <ellipse class="dove-mark" role="img" aria-label="White dove in flight with a soft glow" cx="176" cy="83" rx="62" ry="66" fill="url(#dove-glow)"/>
    </svg>

    <div class="contact">
      <p class="address">4287 Maple Orchard<br>Lane Austin, Texas<span class="zip">78651-2097</span></p>
      <p class="phones"><span class="label">T :</span>512-555-0143<span class="divider"></span>512-555-0178</p>
      <p class="email">dana-whitcombe@examplemail.net</p>
      <p class="web">www.lanternofrenewalbks.com</p>
    </div>

    <h1 class="book-title">Where The River<br>Bends Home</h1>

    <div class="author">
      <p class="name">Dana Whitcombe</p>
      <p class="role">Author</p>
    </div>
  </section>
</body>
</html>
```